Business Card Design For Office Furniture Clearance Company

Kestrel Office Clearance - our company name pretty much explains what we do, we clear offices for high end clients, mainly plc's and large international companies.

We require a nice looking business card that displays professionalism but without being too serious.

It would be nice to see just a little more than a conventional boring business card, make sure you add some flare.

Industry/Entity Type

Office Furniture

Contact Information for Business Card

CARD 1

Tom Pardew
Director
tom@kestrelofficeclearance.co.uk
m: 07700 513928

t: 01632 419063
www.kestrelofficeclearance.co.uk

Kestrel Office Clearance
Unit K4 B
3-7 Ferndale Lane
Ashcombe
Harwick Vale
ZZ9 4QX

free office clearances… you cant get better than that.

CARD 2

Henry Walbrook
Director
henry@kestrelofficeclearance.co.uk
m: 07700 628157

t: 01632 419063

Kestrel Office Clearance
Unit K4 B
3-7 Ferndale Lane
Ashcombe
Harwick Vale
ZZ9 4QX

Font styles to use
Sans Serif

Requirements
Must have
• A white background - as we have a blue logo.
Nice to have
• Nice use of the logo - play around with this and dissect it.

```html
<!DOCTYPE html>
<html lang="en">
<head>
<meta charset="utf-8">
<title>Kestrel Office Clearance – Business Card</title>
<link href="https://fonts.googleapis.com/css2?family=Lato:wght@400;700&display=swap" rel="stylesheet">
<style>
  :root {
    --page-bg: #ececec;
    --card-white: #ffffff;
    --brand-blue: #1a75bb;
    --brand-blue-light: #2a86c9;
    --back-blue: #0a7cc1;
    --text-white: #ffffff;
  }
  * { margin: 0; padding: 0; box-sizing: border-box; }
  html, body {
    width: 1138px; height: 1200px; overflow: hidden;
    background: var(--page-bg);
    font-family: "Lato", sans-serif;
  }
  .card {
    position: absolute; left: 234px;
    width: 670px; height: 384px;
    border-radius: 16px; overflow: hidden;
    box-shadow: 0 3px 10px rgba(0,0,0,0.18);
  }
  .card-front { top: 198px; background: var(--card-white); }
  .card-back { top: 618px; background: var(--back-blue); }

  .colour-field { position: absolute; inset: 0; width: 670px; height: 384px; }

  .brand { position: absolute; left: 0; top: 34px; width: 290px; text-align: center; }
  .brand-mark {
    width: 132px; height: 132px; border-radius: 50%;
    background: var(--brand-blue); margin: 0 auto 12px;
  }
  .brand-name { color: var(--brand-blue); font-weight: 700; font-size: 22px; }

  .contact {
    position: absolute; right: 32px; top: 154px;
    text-align: right; color: var(--text-white);
  }
  .person-name { font-weight: 700; font-size: 24px; line-height: 1.1; }
  .person-role { font-size: 15px; margin-bottom: 20px; }
  .contact-line {
    display: flex; justify-content: flex-end; align-items: center; gap: 8px;
    font-size: 15px; line-height: 21px;
  }
  .contact-line svg { width: 15px; height: 15px; flex: none; }
  .address { margin-top: 10px; font-size: 15px; line-height: 20px; }

  .back-name {
    position: absolute; left: 0; right: 0; top: 160px;
    text-align: center; color: var(--text-white);
    font-weight: 700; font-size: 40px;
  }
  .back-web {
    position: absolute; left: 0; right: 0; bottom: 22px;
    text-align: center; color: var(--text-white); font-size: 15px;
  }
</style>
</head>
<body>

<section class="card card-front">
  <svg class="colour-field" viewBox="0 0 670 384" role="img" aria-label="Blue colour field with a curved upper edge behind the contact details">
    <defs>
      <linearGradient id="field-gradient" x1="0" y1="0" x2="1" y2="1">
        <stop offset="0" stop-color="var(--brand-blue-light)"/>
        <stop offset="1" stop-color="var(--brand-blue)"/>
      </linearGradient>
    </defs>
    <path d="M0,300 C150,330 300,300 420,200 C500,135 580,105 670,105 L670,384 L0,384 Z" fill="url(#field-gradient)"/>
  </svg>

  <div class="brand">
    <div class="brand-mark"></div>
    <div class="brand-name">Kestrel Office Clearance</div>
  </div>

  <div class="contact">
    <div class="person-name">Tom Pardew</div>
    <div class="person-role">Director</div>
    <div class="contact-line">07700 513928
      <svg viewBox="0 0 16 16"><rect x="4" y="1" width="8" height="14" rx="1.5" fill="none" stroke="currentColor" stroke-width="1.5"/><circle cx="8" cy="12.5" r="0.9" fill="currentColor"/></svg>
    </div>
    <div class="contact-line">01632 419063
      <svg viewBox="0 0 16 16"><path d="M4 1.5 L6.5 4.5 L5 6.5 C6 8.5 7.5 10 9.5 11 L11.5 9.5 L14.5 12 L12.5 14.5 C7 14 2 9 1.5 3.5 Z" fill="currentColor"/></svg>
    </div>
    <div class="contact-line">tom@kestrelofficeclearance.co.uk
      <svg viewBox="0 0 16 16"><rect x="1" y="3" width="14" height="10" fill="currentColor"/><path d="M1 3 L8 9 L15 3" fill="none" stroke="var(--brand-blue)" stroke-width="1.3"/></svg>
    </div>
    <div class="contact-line">www.kestrelofficeclearance.co.uk
      <svg viewBox="0 0 16 16" fill="none" stroke="currentColor" stroke-width="1.2"><circle cx="8" cy="8" r="6.5"/><ellipse cx="8" cy="8" rx="3" ry="6.5"/><path d="M1.5 8 H14.5 M2.5 4.8 H13.5 M2.5 11.2 H13.5"/></svg>
    </div>
    <div class="address">Unit K4 B, 3-7 Ferndale Lane Ashcombe<br>Harwick Vale ZZ9 4QX</div>
  </div>
</section>

<section class="card card-back">
  <div class="back-name">Kestrel Office Clearance</div>
  <div class="back-web">www.kestrelofficeclearance.co.uk</div>
</section>

</body>
</html>
```